Brightvale Fire Solutions business card, logo and web design.

We need business cards for our new company. We are based in South Africa. We specialise in fire detection, fire prevention, security, access control and CCTV in buildings. We service and install sprinkler systems, fire hose reals and fire extinguishers in buildings. Our slogan in the company is "Compliance is our business" . We strive to be innovators in our field and deliver the best service possible at the best quality. We want to be the best in our field. We don't have any colour preferences as long as it relates to our type of business.
Our target market is clients that owns big buildings with multiple levels, such a malls,office buildings or warehouses.

Target Market(s)

Industry/Entity Type

Fire Safety

Contact Information for Business Card

The front of the card should have the company name (Brightvale Fire Solutions (PTY) LTD. and a description of the company. Fire engineering & security services.

Logo Text

Compliance is our business

Number of Pages Required

4 page

Font styles to use
Serif

Colors

Designer to choose colors to be used in the design.

Requirements
Must have
• The company name, the logo and all the details on the back of the card. It should be simple and not to busy.
Nice to have
• Just something different and new. Brightvale means - innovate so the card should represent our name.
Should not have
• Small pictures or lots of graphics on.

```html
<!DOCTYPE html>
<html lang="en">
<head>
<meta charset="utf-8">
<title>Brightvale Fire Solutions – Business Card</title>
<link rel="stylesheet" href="https://fonts.googleapis.com/css2?family=Rajdhani:wght@500&family=Oswald:wght@500&family=Lato:wght@400&display=swap">
<style>
  :root {
    --backdrop: #3b3b3b;
    --card-black: #141414;
    --card-sheen: #2a2a2a;
    --card-white: #ffffff;
    --ink-white: #ffffff;
    --accent: #f0782a;
    --ink-grey: #6f6f6f;
  }
  * { margin: 0; padding: 0; box-sizing: border-box; }
  html, body { width: 1200px; height: 1000px; overflow: hidden; }
  body { background: var(--backdrop); position: relative; font-family: "Lato", sans-serif; }

  .card { position: absolute; left: 270px; width: 661px; height: 379px; box-shadow: 0 6px 18px rgba(0,0,0,.35); }

  .card-front {
    top: 108px;
    background: linear-gradient(118deg, var(--card-black) 0%, var(--card-black) 50%, var(--card-sheen) 58%, #1b1b1b 72%, var(--card-black) 100%);
    text-align: center;
    color: var(--ink-white);
  }
  .brand-name {
    position: absolute; top: 140px; left: 0; right: 0;
    font-family: "Rajdhani", sans-serif; font-weight: 500;
    font-size: 66px; line-height: 1; letter-spacing: 1px;
  }
  .brand-sub {
    position: absolute; top: 214px; left: 0; right: 0;
    font-family: "Rajdhani", sans-serif; font-weight: 500;
    font-size: 23px; letter-spacing: 3.2px;
  }
  .brand-services {
    position: absolute; top: 320px; left: 0; right: 0;
    font-size: 17px; color: var(--accent);
  }

  .card-back { top: 521px; background: var(--card-white); color: var(--ink-grey); }
  .person-name {
    position: absolute; left: 43px; top: 130px;
    font-family: "Oswald", sans-serif; font-weight: 500;
    font-size: 26px; color: var(--accent); line-height: 1;
  }
  .person-role { position: absolute; left: 43px; top: 166px; font-size: 15px; }
  .role-rule { position: absolute; left: 43px; top: 194px; width: 32px; height: 2px; background: var(--accent); }
  .address {
    position: absolute; left: 43px; top: 226px;
    font-size: 15px; letter-spacing: .4px; white-space: nowrap;
  }
  .divider { position: absolute; left: 43px; width: 575px; height: 1px; background: var(--accent); }
  .divider-top { top: 259px; }
  .divider-bottom { top: 304px; }
  .contacts {
    position: absolute; left: 43px; top: 272px; width: 575px;
    display: flex; justify-content: space-between; font-size: 15px; white-space: nowrap;
  }
  .contact { display: flex; align-items: center; gap: 5px; }
  .contact svg { width: 12px; height: 12px; fill: #333; }
  .registration { position: absolute; left: 43px; top: 320px; font-size: 15px; }
</style>
</head>
<body>
  <section class="card card-front">
    <div class="brand-name">BRIGHTVALE</div>
    <div class="brand-sub">FIRE SOLUTIONS (PTY) LTD</div>
    <div class="brand-services">FIRE ENGINEERING &amp; SECURITY SERVICES</div>
  </section>

  <section class="card card-back">
    <div class="person-name">PIETER VENTER</div>
    <div class="person-role">MANAGING DIRECTOR</div>
    <div class="role-rule"></div>
    <div class="address">18 MARULA STREET&nbsp; .&nbsp; LYNNWOOD RIDGE&nbsp; .&nbsp; PRETORIA&nbsp; .&nbsp; 0081&nbsp; .&nbsp; SOUTH AFRICA</div>
    <div class="divider divider-top"></div>
    <div class="contacts">
      <span class="contact">
        <svg viewBox="0 0 12 12" aria-hidden="true"><path d="M2.5 0.5 L4.5 3 L3.4 4.3 Q4.5 6.8 7.6 8.6 L8.9 7.5 L11.5 9.5 L10 11.5 Q4.5 11 0.5 2 Z"/></svg>012-555-0142
      </span>
      <span class="contact">
        <svg viewBox="0 0 12 12" aria-hidden="true"><path d="M3 0 H9 V12 H3 Z M4 1.2 V9.5 H8 V1.2 Z"/></svg>082-555-0176
      </span>
      <span class="contact">
        <svg viewBox="0 0 12 12" aria-hidden="true"><path d="M3 1 H9 V4 H11 V10 H9 V8 H3 V10 H1 V4 H3 Z M4 2 V4 H8 V2 Z M4 9 H8 V11 H4 Z"/></svg>012-555-0199
      </span>
      <span class="contact">
        <svg viewBox="0 0 12 12" aria-hidden="true"><path d="M0.5 2.5 H11.5 V9.5 H0.5 Z M1.2 3 L6 6.6 L10.8 3 Z"/></svg>info@brightvale.com
      </span>
    </div>
    <div class="divider divider-bottom"></div>
    <div class="registration">VAT NO: 4710385526&nbsp; .&nbsp; REG NO: 21/048317/07</div>
  </section>
</body>
</html>
```